Elegant Black Candle Label Design!

I need a 2.375" tall by 3.0" wide candle label design. I'm looking for simple and elegant. Black label with silver leaf border and lettering. Label needs to have the following information on it: Fern Hollow Candle Co. as the company name, scent name in the middle and in smaller font, it needs to say Made in USA, All Natural, 8oz. Attached photos are for inspiration.

Target Market(s)

People looking for high end, all natural candle fragrances

Industry/Entity Type

Candle-Spa

Colors

Designer to choose only greyscale colors for use in the design.

Requirements
Must have
• Company Name, Scent (ability to change scent names), All Natural, Made in USA, 8oz
Nice to have
• Black background, silver leaf border and silver leaf font. Elegant fonts maybe slightly cursive

```html
<!DOCTYPE html>
<html lang="en">
<head>
<meta charset="utf-8">
<title>Fern Hollow Candle Co. – Label</title>
<link href="https://fonts.googleapis.com/css2?family=Josefin+Sans:wght@400;600&display=swap" rel="stylesheet">
<style>
  :root {
    --backdrop: #e8e6e2;
    --label-black: #0c0c0c;
    --silver-light: #e6e6e6;
    --silver-mid: #a9a9a9;
    --silver-dark: #5e5e5e;
    --ink-white: #f4f4f4;
  }
  html, body {
    margin: 0;
    width: 1200px;
    height: 1200px;
    overflow: hidden;
    background: var(--backdrop);
  }
  .canvas {
    position: relative;
    width: 1200px;
    height: 1200px;
  }
  .label {
    position: absolute;
    left: 100px;
    top: 204px;
    width: 1000px;
    height: 792px;
  }
  .silver-leaf-border {
    position: absolute;
    inset: 0;
    background: linear-gradient(135deg, var(--silver-light) 0%, var(--silver-mid) 30%, var(--silver-light) 50%, var(--silver-dark) 78%, var(--silver-light) 100%);
  }
  .label-panel {
    position: absolute;
    inset: 30px;
    background: var(--label-black);
  }
  .panel-frame {
    position: absolute;
    inset: 14px;
    border: 2px solid var(--ink-white);
  }
  .text-line {
    position: absolute;
    left: 0;
    right: 0;
    text-align: center;
    color: var(--ink-white);
    font-family: "Josefin Sans", sans-serif;
    line-height: 1;
  }
  .brand-mark {
    top: 62px;
    font-size: 26px;
    font-weight: 600;
    letter-spacing: 2px;
    display: flex;
    justify-content: center;
    align-items: center;
    gap: 12px;
  }
  .brand-mark .dot {
    width: 16px;
    height: 16px;
    border-radius: 50%;
    background: var(--ink-white);
  }
  .company-name {
    top: 124px;
    font-size: 64px;
    font-weight: 600;
    letter-spacing: 1px;
  }
  .company-suffix {
    top: 204px;
    font-size: 48px;
    font-weight: 600;
  }
  .rule {
    position: absolute;
    left: 200px;
    right: 200px;
    height: 2px;
    background: var(--ink-white);
  }
  .rule-top { top: 284px; }
  .rule-bottom { top: 592px; }
  .scent-name {
    top: 318px;
    font-size: 40px;
    font-weight: 400;
    letter-spacing: 3px;
  }
  .detail {
    font-size: 30px;
    font-weight: 400;
  }
  .detail-origin { top: 400px; }
  .detail-natural { top: 457px; }
  .detail-weight { top: 514px; }
  .footer-note {
    top: 624px;
    font-size: 15px;
    letter-spacing: 1px;
  }
</style>
</head>
<body>
<div class="canvas">
  <div class="label">
    <div class="silver-leaf-border" role="img" aria-label="Silver leaf foliage pattern border"></div>
    <div class="label-panel">
      <div class="panel-frame"></div>
      <div class="text-line brand-mark"><span class="dot"></span><span>FERN HOLLOW</span></div>
      <div class="text-line company-name">FERN HOLLOW</div>
      <div class="text-line company-suffix">CANDLE CO.</div>
      <div class="rule rule-top"></div>
      <div class="text-line scent-name">LAVENDER &amp; SAGE</div>
      <div class="text-line detail detail-origin">MADE IN USA</div>
      <div class="text-line detail detail-natural">ALL NATURAL</div>
      <div class="text-line detail detail-weight">8oz</div>
      <div class="rule rule-bottom"></div>
      <div class="text-line footer-note">HAND POURED SMALL BATCH CANDLES</div>
    </div>
  </div>
</div>
</body>
</html>
```